Now Open Poster

We need a banner for our sports supplement and nutritional store, Harbor Nutrition.
We were hoping for some sort of creative word art piece.
I have drawn my own mock up just to give you all a very basic starting point. But you are free to go with whatever you feel will work best.
The primary objective is simply to explain a little about what the company does, and then direct traffic towards the store with an 'Open Arrow' pointing left.
Text words we have chosen are:
Protein
Creatine
Health
Fitness
Sports Science
Nutrition
Energy
Achievement
Amino Acids
Organic
Supplements
Performance
Testosterone Support
Vitamins
Growth
Diet
Happiness
Weight Loss
Strong
Natural
Vitality
Accomplished
Below the word art we want our logo (See attached options)
Then below the logo the phrase "Success Starts Here"
Dimensions of the poster are 140cm x 60cm.
Colours: Blues/Whites/Greys/Blacks (Lots of white space please)
Here are some cool pieces I found that had some interesting elements that I liked (I'd love to see a mash-up of styles with a street art feel to it. Something funky!):
http://www.moodgrove.example/pin/804417263190552871/
http://www.moodgrove.example/pin/615380924471208539/
http://www.moodgrove.example/pin/804417263192736155/
http://www.moodgrove.example/pin/804417263194418620/
http://www.moodgrove.example/pin/937162048856301742/
Thanks for reading, message me if you have any further questions!
- Tobias

```html
<!DOCTYPE html>
<html lang="en">
<head>
<meta charset="utf-8">
<title>Harbor Nutrition – Now Open Banner</title>
<link rel="stylesheet" href="https://fonts.googleapis.com/css2?family=Michroma&family=Six+Caps&family=Big+Shoulders+Display:wght@600;800&family=Ubuntu:wght@500;700&family=Oswald:wght@400&display=swap">
<style>
  :root {
    --stage: #ececed;
    --paper: #ffffff;
    --ink: #353d3b;
    --navy: #3f6282;
    --steel: #5b8ba6;
    --sky: #7ea8bf;
    --stone: #9f9b95;
    --sage: #6e9e8c;
    --rule: #b9b9bb;
    --black: #111111;
  }
  * { margin: 0; padding: 0; box-sizing: border-box; }
  html, body { width: 1200px; height: 1000px; overflow: hidden; }
  body { background: var(--stage); position: relative; }

  .divider { position: absolute; left: 609px; top: 55px; width: 1px; height: 893px; background: var(--rule); }

  .banner { position: absolute; top: 55px; width: 384px; height: 893px; background: var(--paper); overflow: hidden; }
  .banner--plain { left: 133px; }
  .banner--textured { left: 699px; }
  .banner__texture { position: absolute; inset: 0;
    background: radial-gradient(ellipse at 30% 20%, #f3f6f6 0%, #e3e9ea 45%, #d3dcde 100%); }
  .banner__art { position: absolute; left: 0; top: 0; width: 384px; height: 893px; }

  .f-wide { font-family: "Michroma", sans-serif; }
  .f-tall { font-family: "Six Caps", sans-serif; }
  .f-cond { font-family: "Big Shoulders Display", sans-serif; font-weight: 800; }
  .f-cond-light { font-family: "Big Shoulders Display", sans-serif; font-weight: 600; }
  .f-sans { font-family: "Ubuntu", sans-serif; font-weight: 700; }
  .f-narrow { font-family: "Oswald", sans-serif; font-weight: 400; }

  .c-ink { fill: var(--ink); }
  .c-navy { fill: var(--navy); }
  .c-steel { fill: var(--steel); }
  .c-sky { fill: var(--sky); }
  .c-stone { fill: var(--stone); }
  .c-sage { fill: var(--sage); }
  .c-black { fill: var(--black); }
  .outline { fill: none; stroke-width: 1.3; }
  .o-sky { stroke: var(--sky); }
  .o-steel { stroke: var(--steel); }
  .o-stone { stroke: var(--stone); }

  .brand-mark { position: absolute; left: 121px; top: 650px; width: 142px; height: 142px; border: 2px solid var(--black); border-radius: 50%; display: flex; align-items: center; justify-content: center; text-align: center; }
  .brand-mark__name { font-family: "Michroma", sans-serif; font-size: 12px; line-height: 1.5; color: var(--black); letter-spacing: 1px; }
</style>
</head>
<body>

<svg width="0" height="0" style="position:absolute" aria-hidden="true">
  <defs>
    <symbol id="chevrons" viewBox="0 0 56 22">
      <g class="c-ink"><polygon points="10,0 18,0 8,11 18,22 10,22 0,11"/><polygon points="29,0 37,0 27,11 37,22 29,22 19,11"/><polygon points="48,0 56,0 46,11 56,22 48,22 38,11"/></g>
    </symbol>
    <symbol id="word-art" viewBox="0 0 384 893">
      <use href="#chevrons" x="41" y="42" width="56" height="22"/>
      <text class="f-wide c-ink" x="125" y="64" font-size="28" textLength="137" lengthAdjust="spacingAndGlyphs">OPEN</text>
      <use href="#chevrons" x="289" y="42" width="56" height="22"/>

      <text class="f-cond outline o-sky" x="40" y="135" font-size="46" textLength="174" lengthAdjust="spacingAndGlyphs">PROTEIN</text>
      <text class="f-cond c-navy" x="229" y="133" font-size="40" textLength="116" lengthAdjust="spacingAndGlyphs">FITNESS</text>
      <text class="f-tall c-navy" x="40" y="235" font-size="100" textLength="122" lengthAdjust="spacingAndGlyphs">SPORTS</text>
      <text class="f-cond-light outline o-steel" x="172" y="217" font-size="87" textLength="173" lengthAdjust="spacingAndGlyphs">HEALTH</text>
      <text class="f-cond c-stone" x="40" y="288" font-size="42" textLength="120" lengthAdjust="spacingAndGlyphs">CREATINE</text>
      <text class="f-tall outline o-sky" x="172" y="290" font-size="67" textLength="93" lengthAdjust="spacingAndGlyphs">SCIENCE</text>
      <text class="f-cond c-navy" x="280" y="252" font-size="25" textLength="65" lengthAdjust="spacingAndGlyphs">ENERGY</text>
      <text class="f-cond-light outline o-sky" x="280" y="288" font-size="36" textLength="65" lengthAdjust="spacingAndGlyphs">GROWTH</text>
      <text class="f-cond outline o-steel" x="40" y="337" font-size="45" textLength="224" lengthAdjust="spacingAndGlyphs">NUTRITION</text>
      <text class="f-cond c-stone" x="280" y="335" font-size="39" textLength="65" lengthAdjust="spacingAndGlyphs">DIET</text>
      <text class="f-cond-light c-stone" x="40" y="373" font-size="29" textLength="62" lengthAdjust="spacingAndGlyphs">WEIGHT</text>
      <text class="f-cond c-sky" x="40" y="422" font-size="48" textLength="64" lengthAdjust="spacingAndGlyphs">LOSS</text>
      <text class="f-tall c-navy" x="117" y="422" font-size="83" textLength="142" lengthAdjust="spacingAndGlyphs">HAPPINESS</text>
      <text class="f-cond c-sky" x="280" y="375" font-size="30" textLength="65" lengthAdjust="spacingAndGlyphs">STRONG</text>
      <text class="f-cond outline o-stone" x="280" y="421" font-size="31" textLength="65" lengthAdjust="spacingAndGlyphs">NATURAL</text>
      <text class="f-tall c-navy" x="40" y="463" font-size="29" textLength="62" lengthAdjust="spacingAndGlyphs">AMINO ACIDS</text>
      <text class="f-cond c-steel" x="120" y="465" font-size="36" textLength="142" lengthAdjust="spacingAndGlyphs">ACHIEVEMENT</text>
      <text class="f-cond-light outline o-steel" x="280" y="463" font-size="34" textLength="65" lengthAdjust="spacingAndGlyphs">VITAMINS</text>
      <text class="f-sans c-navy" x="40" y="493" font-size="22" textLength="131" lengthAdjust="spacingAndGlyphs">PERFORMANCE</text>
      <text class="f-narrow c-sage" x="194" y="491" font-size="16" textLength="151" lengthAdjust="spacingAndGlyphs">TESTOSTERONE SUPPORT</text>
      <text class="f-tall c-stone" x="40" y="543" font-size="44" textLength="64" lengthAdjust="spacingAndGlyphs">ORGANIC</text>
      <text class="f-cond outline o-sky" x="119" y="545" font-size="48" textLength="226" lengthAdjust="spacingAndGlyphs">SUPPLEMENTS</text>

      <text class="f-sans c-navy" x="35" y="623" font-size="95" textLength="57" lengthAdjust="spacingAndGlyphs">A</text>
      <polygon class="c-sky" points="95,565 115,565 115,581 95,581 102,573"/>
      <text class="f-narrow c-steel" x="122" y="585" font-size="36" textLength="145" lengthAdjust="spacing">VITALITY</text>
      <polygon class="c-sky" points="272,565 292,565 285,573 292,581 272,581"/>
      <text class="f-sans c-navy" x="93" y="623" font-size="40" textLength="199" lengthAdjust="spacingAndGlyphs">CCOMPLISHE</text>
      <text class="f-sans c-navy" x="297" y="623" font-size="95" textLength="53" lengthAdjust="spacingAndGlyphs">D</text>

      <text class="f-wide c-black" x="66" y="833" font-size="17" textLength="253" lengthAdjust="spacingAndGlyphs">SUCCESS STARTS</text>
      <text class="f-wide c-black" x="151" y="862" font-size="17" textLength="85" lengthAdjust="spacingAndGlyphs">HERE.</text>
    </symbol>
  </defs>
</svg>

<div class="divider"></div>

<section class="banner banner--plain">
  <svg class="banner__art" viewBox="0 0 384 893" role="img" aria-label="Now open: protein, fitness, sports, health, creatine, science, energy, growth, nutrition, diet, weight loss, happiness, strong, natural, amino acids, achievement, vitamins, performance, testosterone support, organic, supplements, vitality, accomplished. Success starts here."><use href="#word-art"/></svg>
  <div class="brand-mark"><span class="brand-mark__name">HARBOR<br>NUTRITION</span></div>
</section>

<section class="banner banner--textured">
  <div class="banner__texture" role="img" aria-label="Pale grey-blue weathered grunge texture"></div>
  <svg class="banner__art" viewBox="0 0 384 893" role="img" aria-label="Now open word-art banner, textured version. Success starts here."><use href="#word-art"/></svg>
  <div class="brand-mark"><span class="brand-mark__name">HARBOR<br>NUTRITION</span></div>
</section>

</body>
</html>
```